Create a memorable Stationary for Security Software Company

TelVandrik is the worldwide leader in securing the Internet. Making Internet communications and critical data secure, reliable and available everywhere has been and continues to be our ongoing vision. We are committed to staying focused on real customer needs and to developing new and innovative security solutions that redefine the security landscape.

Industry/Entity Type

Internet

Font styles to use
Serif
Sans Serif
Script

Colors
0792cd
33a6d7
85cae6

```html
<!DOCTYPE html>
<html lang="en">
<head>
<meta charset="utf-8">
<title>TelVandrik Stationery</title>
<link rel="stylesheet" href="https://fonts.googleapis.com/css2?family=Didact+Gothic&family=Montserrat:wght@400;600&display=swap">
<style>
:root{
  --blue-deep:#0a7fb6;
  --blue:#0792cd;
  --blue-mid:#33a6d7;
  --blue-light:#85cae6;
  --ink:#4a4a4a;
  --paper:#ffffff;
  --edge:#d9d9d9;
}
*{margin:0;padding:0;box-sizing:border-box}
html,body{width:1200px;height:1200px;overflow:hidden;background:var(--paper)}
body{position:relative;font-family:"Didact Gothic",sans-serif;color:var(--ink)}
.piece{position:absolute;background:var(--paper);box-shadow:0 1px 4px rgba(0,0,0,.22);overflow:hidden}
.piece>svg.art{position:absolute;left:0;top:0}
.brand{position:absolute;text-align:center;transform:translateX(-50%)}
.brand-name{display:inline-flex;align-items:center;gap:4px;font-family:"Didact Gothic",sans-serif;color:var(--blue);white-space:nowrap;line-height:1}
.brand-dot{display:inline-block;border-radius:50%;background:var(--blue)}
.brand-sub{display:block;font-family:"Montserrat",sans-serif;color:var(--ink);white-space:nowrap}
.contact{position:absolute;font-family:"Montserrat",sans-serif;color:var(--ink)}
.contact li{list-style:none;display:flex;align-items:center;justify-content:flex-end;white-space:nowrap}
.contact svg{fill:var(--blue-mid);flex:none}

.letterhead{left:132px;top:130px;width:432px;height:560px}
.letterhead .brand{left:140px;top:48px}
.letterhead .brand-name{font-size:19px}
.letterhead .brand-dot{width:9px;height:9px}
.letterhead .brand-sub{font-size:7px;margin-top:5px}
.letterhead .footer-band{position:absolute;left:0;bottom:0;width:100%;height:11px;background:var(--blue-mid)}
.letterhead .contact{left:0;right:0;top:527px;display:flex;justify-content:flex-end;gap:12px;padding-right:28px;font-size:5px}
.letterhead .contact li{gap:3px}

.folder{left:719px;top:136px;width:305px;height:306px}
.folder .brand{left:154px;top:232px}
.folder .brand-name{font-size:17px}
.folder .brand-dot{width:8px;height:8px}
.folder .brand-sub{font-size:7px;margin-top:5px}

.disc{left:717px;top:510px;width:288px;height:288px;border-radius:50%;box-shadow:0 0 0 1px var(--edge),0 1px 4px rgba(0,0,0,.2)}
.disc .brand{left:144px;top:222px}
.disc .brand-name{font-size:14px}
.disc .brand-dot{width:7px;height:7px}
.disc .brand-sub{font-size:6px;margin-top:4px}

.card-back{left:132px;top:725px;width:192px;height:109px}
.card-back .holder{position:absolute;right:14px;top:18px;text-align:right;font-family:"Montserrat",sans-serif}
.card-back .holder-name{font-size:11px;font-weight:600;color:var(--blue)}
.card-back .holder-role{font-size:5px;color:var(--ink)}
.card-back .contact{right:14px;top:56px;font-size:4.5px}
.card-back .contact li{gap:4px;margin-bottom:6px}

.card-front{left:374px;top:725px;width:190px;height:109px}
.card-front .brand{left:64px;top:64px}
.card-front .brand-name{font-size:11px}
.card-front .brand-dot{width:5px;height:5px}
.card-front .brand-sub{font-size:5px;margin-top:3px}

.envelope-front{left:132px;top:874px;width:427px;height:194px}
.envelope-front .brand{left:370px;top:36px}
.envelope-front .brand-name{font-size:16px}
.envelope-front .brand-dot{width:8px;height:8px}
.envelope-front .brand-sub{font-size:7px;margin-top:5px}
.envelope-front .contact{right:24px;top:130px;font-size:5px}
.envelope-front .contact li{gap:5px;margin-bottom:5px}

.envelope-back{left:658px;top:874px;width:426px;height:194px;box-shadow:0 0 0 1px #9a9a9a}
.envelope-back svg{position:absolute;left:0;top:0}
</style>
</head>
<body>

<svg width="0" height="0" style="position:absolute" aria-hidden="true">
  <defs>
    <symbol id="icon-phone" viewBox="0 0 10 10"><path d="M2 1h2l1 2-1.2 1a6 6 0 0 0 2.2 2.2L7 5l2 1v2a1 1 0 0 1-1 1A8 8 0 0 1 1 2a1 1 0 0 1 1-1z"/></symbol>
    <symbol id="icon-mail" viewBox="0 0 10 10"><path d="M1 2h8v6H1z M1.5 2.5 5 5.5 8.5 2.5" stroke="#fff" stroke-width=".8"/></symbol>
    <symbol id="icon-web" viewBox="0 0 10 10"><circle cx="5" cy="5" r="4"/><path d="M1 5h8M5 1c2 2 2 6 0 8M5 1c-2 2-2 6 0 8" stroke="#fff" stroke-width=".6" fill="none"/></symbol>
    <symbol id="icon-pin" viewBox="0 0 10 10"><path d="M5 0.5a3.3 3.3 0 0 1 3.3 3.3C8.3 6.5 5 9.5 5 9.5S1.7 6.5 1.7 3.8A3.3 3.3 0 0 1 5 .5z"/><circle cx="5" cy="3.8" r="1.2" fill="#fff"/></symbol>
  </defs>
</svg>

<section class="piece letterhead" aria-label="Letterhead">
  <svg class="art" width="432" height="100" viewBox="0 0 432 100" role="img" aria-label="Layered blue geometric header artwork">
    <defs><linearGradient id="grad-letterhead" x1="0" y1="0" x2="1" y2="0"><stop offset="0" stop-color="var(--blue-deep)"/><stop offset=".55" stop-color="var(--blue-mid)"/><stop offset="1" stop-color="var(--blue-light)"/></linearGradient></defs>
    <polygon points="0,0 432,0 432,98 156,26 0,86" fill="url(#grad-letterhead)"/>
  </svg>
  <div class="brand"><span class="brand-name"><span class="brand-dot"></span>TelVandrik</span><span class="brand-sub">Sub Text Here</span></div>
  <ul class="contact">
    <li><svg width="7" height="7"><use href="#icon-pin"/></svg>No Street, Avenue, City, State Zip Code</li>
    <li><svg width="7" height="7"><use href="#icon-mail"/></svg>youremail@domain.com</li>
    <li><svg width="7" height="7"><use href="#icon-web"/></svg>www.yourdomain.com</li>
    <li><svg width="7" height="7"><use href="#icon-phone"/></svg>(00) 123 456 7890</li>
  </ul>
  <div class="footer-band"></div>
</section>

<section class="piece folder" aria-label="Presentation folder">
  <svg class="art" width="305" height="306" viewBox="0 0 305 306" role="img" aria-label="Layered blue geometric cover artwork">
    <defs><linearGradient id="grad-folder" x1="0" y1="1" x2="1" y2="0"><stop offset="0" stop-color="var(--blue-deep)"/><stop offset=".6" stop-color="var(--blue-mid)"/><stop offset="1" stop-color="var(--blue-light)"/></linearGradient></defs>
    <polygon points="0,0 305,0 305,262 145,164 0,262" fill="url(#grad-folder)"/>
  </svg>
  <div class="brand"><span class="brand-name"><span class="brand-dot"></span>TelVandrik</span><span class="brand-sub">Sub Text Here</span></div>
</section>

<section class="piece disc" aria-label="Compact disc">
  <svg class="art" width="288" height="288" viewBox="0 0 288 288" role="img" aria-label="Layered blue geometric disc artwork">
    <defs>
      <clipPath id="disc-clip"><circle cx="144" cy="144" r="144"/></clipPath>
      <linearGradient id="grad-disc" x1="0" y1="1" x2="1" y2="0"><stop offset="0" stop-color="var(--blue-deep)"/><stop offset=".6" stop-color="var(--blue-mid)"/><stop offset="1" stop-color="var(--blue-light)"/></linearGradient>
    </defs>
    <polygon clip-path="url(#disc-clip)" points="0,0 288,0 288,230 144,176 0,230" fill="url(#grad-disc)"/>
    <circle cx="144" cy="144" r="45" fill="var(--paper)" stroke="var(--edge)" stroke-width="1"/>
  </svg>
  <div class="brand"><span class="brand-name"><span class="brand-dot"></span>TelVandrik</span><span class="brand-sub">Sub Text Here</span></div>
</section>

<section class="piece card-back" aria-label="Business card, contact side">
  <svg class="art" width="192" height="109" viewBox="0 0 192 109" role="img" aria-label="Layered blue geometric side artwork">
    <defs><linearGradient id="grad-card-back" x1="0" y1="1" x2="0" y2="0"><stop offset="0" stop-color="var(--blue)"/><stop offset="1" stop-color="var(--blue-light)"/></linearGradient></defs>
    <polygon points="0,0 62,0 44,70 64,109 0,109" fill="url(#grad-card-back)"/>
  </svg>
  <div class="holder"><div class="holder-name">Mara Quill</div><div class="holder-role">general manager</div></div>
  <ul class="contact">
    <li>(00) 123 456 7890<svg width="7" height="7"><use href="#icon-phone"/></svg></li>
    <li>youremail@domain.com<svg width="7" height="7"><use href="#icon-mail"/></svg></li>
    <li>No Street, Avenue, City, State Zip Code<svg width="7" height="7"><use href="#icon-pin"/></svg></li>
  </ul>
</section>

<section class="piece card-front" aria-label="Business card, brand side">
  <svg class="art" width="190" height="109" viewBox="0 0 190 109" role="img" aria-label="Layered blue geometric header artwork">
    <defs><linearGradient id="grad-card-front" x1="0" y1="0" x2="1" y2="0"><stop offset="0" stop-color="var(--blue-deep)"/><stop offset=".55" stop-color="var(--blue-mid)"/><stop offset="1" stop-color="var(--blue-light)"/></linearGradient></defs>
    <polygon points="0,0 190,0 190,70 64,43 0,60" fill="url(#grad-card-front)"/>
  </svg>
  <div class="brand"><span class="brand-name"><span class="brand-dot"></span>TelVandrik</span><span class="brand-sub">Sub Text Here</span></div>
</section>

<section class="piece envelope-front" aria-label="Envelope, address side">
  <svg class="art" width="427" height="194" viewBox="0 0 427 194" role="img" aria-label="Layered blue geometric side artwork">
    <defs><linearGradient id="grad-envelope" x1="0" y1="1" x2="0" y2="0"><stop offset="0" stop-color="var(--blue)"/><stop offset="1" stop-color="var(--blue-light)"/></linearGradient></defs>
    <polygon points="0,0 112,0 52,134 102,194 0,194" fill="url(#grad-envelope)"/>
  </svg>
  <div class="brand"><span class="brand-name"><span class="brand-dot"></span>TelVandrik</span><span class="brand-sub">Sub Text Here</span></div>
  <ul class="contact">
    <li>(00) 123 456 7890<svg width="7" height="7"><use href="#icon-phone"/></svg></li>
    <li>www.yourdomain.com<svg width="7" height="7"><use href="#icon-web"/></svg></li>
    <li>youremail@domain.com<svg width="7" height="7"><use href="#icon-mail"/></svg></li>
    <li>No Street, Avenue, City, State Zip Code<svg width="7" height="7"><use href="#icon-pin"/></svg></li>
  </ul>
</section>

<section class="piece envelope-back" aria-label="Envelope, flap side">
  <svg width="426" height="194" viewBox="0 0 426 194" aria-hidden="true">
    <polygon points="0,0 426,0 408,60 18,60" fill="var(--blue-mid)"/>
  </svg>
</section>

</body>
</html>
```